Need Business Card for our Indian Grocery Store

Industry/Entity Type

Grocery Store

Contact Information for Business Card

Manoj Baweja
Director

Store Locations:

Kelvale
482 Elm Parade
P: 03 9172 5843

Brookmere
613 Carlow Road
P: 03 9238 6014

email: kvtmarts@mailnest.example

Requirements
Must have
• Our logo Colours

```html
<!DOCTYPE html>
<html lang="en">
<head>
<meta charset="utf-8">
<title>KVT Pantry &amp; Masala – Business Card</title>
<link href="https://fonts.googleapis.com/css2?family=Exo+2:wght@400;600;700&family=Libre+Baskerville:ital@1&display=swap" rel="stylesheet">
<style>
  :root {
    --stage: #232826;
    --brand-red: #e2332a;
    --brand-red-light: #ef5a3c;
    --brand-red-dark: #d42a25;
    --paper: #ffffff;
    --ink: #161616;
    --leaf-dark: #2f4a2e;
    --leaf-mid: #5f7f52;
    --veil: rgba(255,255,255,0.82);
  }
  * { box-sizing: border-box; margin: 0; padding: 0; }
  html, body { width: 1200px; height: 1000px; overflow: hidden; }
  body {
    background: var(--stage);
    font-family: "Exo 2", sans-serif;
    position: relative;
  }
  .card {
    position: absolute;
    top: 357px;
    width: 500px;
    height: 286px;
    border-radius: 24px;
    overflow: hidden;
  }
  .card--front { left: 70px; }
  .card--back {
    left: 630px;
    background: linear-gradient(120deg, var(--brand-red-light), var(--brand-red) 45%, var(--brand-red-dark));
  }

  /* Front */
  .produce-photo {
    position: absolute; inset: 0;
    background:
      radial-gradient(circle at 20% 85%, #7fa05f 0%, transparent 40%),
      radial-gradient(circle at 85% 20%, #8a7f70 0%, transparent 45%),
      linear-gradient(135deg, var(--leaf-mid), var(--leaf-dark) 60%, #3b4a44);
  }
  .veil-circle {
    position: absolute;
    left: 55px; top: -60px;
    width: 400px; height: 400px;
    border-radius: 50%;
    background: var(--veil);
    border: 2px solid var(--brand-red);
  }
  .brand-lockup {
    position: absolute;
    left: 55px; width: 400px; top: 62px;
    text-align: center;
    color: var(--brand-red);
  }
  .brand-name {
    font-weight: 700;
    font-size: 84px;
    line-height: 1;
    letter-spacing: 4px;
  }
  .brand-category {
    margin-top: 10px;
    font-weight: 600;
    font-size: 20px;
    letter-spacing: 3px;
    text-transform: uppercase;
  }
  .brand-tagline {
    margin-top: 8px;
    font-family: "Libre Baskerville", serif;
    font-style: italic;
    font-size: 15px;
  }

  /* Back */
  .label-frame { position: absolute; inset: 0; }
  .contact {
    position: absolute; inset: 0;
    color: var(--ink);
    text-align: center;
  }
  .contact__name {
    position: absolute; top: 68px; left: 0; right: 0;
    font-weight: 700; font-size: 22px; letter-spacing: 1px;
    text-transform: uppercase;
  }
  .contact__role {
    position: absolute; top: 96px; left: 0; right: 0;
    font-size: 12px;
  }
  .stores {
    position: absolute; top: 126px; left: 0; right: 0;
    display: flex; justify-content: center; gap: 22px;
  }
  .store { font-weight: 600; font-size: 14px; line-height: 1.3; width: 150px; }
  .store--left { text-align: right; }
  .store--right { text-align: left; }
  .store__divider { width: 2px; background: var(--ink); }
  .contact__email {
    position: absolute; top: 206px; left: 0; right: 0;
    font-weight: 600; font-size: 14px;
  }
</style>
</head>
<body>
  <section class="card card--front">
    <div class="produce-photo" role="img" aria-label="Photograph of fresh leafy greens and vegetables at a market stall"></div>
    <div class="veil-circle"></div>
    <div class="brand-lockup">
      <div class="brand-name">KVT</div>
      <div class="brand-category">Pantry &amp; Masala</div>
      <div class="brand-tagline">Fresh Picks Every Day</div>
    </div>
  </section>

  <section class="card card--back">
    <svg class="label-frame" viewBox="0 0 500 286" width="500" height="286" aria-hidden="true">
      <path fill="var(--paper)" d="M44,26 Q250,50 456,26 Q480,24 478,50 Q468,143 478,236 Q480,262 456,260 Q250,236 44,260 Q20,262 22,236 Q32,143 22,50 Q20,24 44,26Z"/>
      <path fill="none" stroke="var(--brand-red)" stroke-width="2.5" d="M50,36 Q250,58 450,36 Q468,35 467,54 Q458,143 467,232 Q468,251 450,250 Q250,228 50,250 Q32,251 33,232 Q42,143 33,54 Q32,35 50,36Z"/>
    </svg>
    <div class="contact">
      <div class="contact__name">Manoj Baweja</div>
      <div class="contact__role">Director</div>
      <div class="stores">
        <div class="store store--left">Kelvale<br>482 Elm Parade<br>P: 03 9172 5843</div>
        <div class="store__divider"></div>
        <div class="store store--right">Brookmere<br>613 Carlow Road<br>P: 03 9238 6014</div>
      </div>
      <div class="contact__email">kvtmarts@mailnest.example</div>
    </div>
  </section>
</body>
</html>
```